Flyer für Alpaka und Lama Hof
Zielgruppe
Landwirtschaftlicher Betrieb mit Alpakahaltung seit 2021.
Wir bieten an
Alpaka- und LamaWanderungen,
Picknick mit Alpakas und Lamas
Schnupperstunden / Kennenlernen
Betriebsausflüge & Gruppenangebote
Junggesellenabschiede
Persönlich geführt, familiär, mit viel Herzblut und echter Begeisterung für Alpakas und Lamas
Familien, Paare, Betriebe & Teams, Freundesgruppen, Junggesellenabschiede
Tier- & Naturliebhaber,
Menschen, die Alpakas/Lamas lieben oder kennenlernen möchten
Aufgabenstellung
Ziel ist die Gestaltung eines Flyers für ein Alpaka-/Lama Angebot (z. B. Wanderungen, Begegnungen, Erlebnisse), der emotional anspricht, Vertrauen schafft und Lust auf ein besonderes Natur- und Tiererlebnis macht.
Der Flyer kann sich am bestehenden Flyer sowie am Design der Visitenkarten und Gutscheine (mit hochgeladen)orientieren, ohne diese exakt zu kopieren. Der Flyer soll ein 6-seitiger Wickelfalz sein.
Die Texte in meinem hochgeladenen Flyer sind Bausteine und unvollständig. Sie müssen nicht unbedingt verwendet werden und dürfen angepasst werden. Im Flyer soll klar kommuniziert werden, dass alle Alpaka-/Lama Erlebnisse auch als Gutscheine erhältlich sind aber ohne werbliche Sprache.
Ich bin für Text Änderungen offen.

```html
<!DOCTYPE html>
<html lang="de">
<head>
<meta charset="utf-8">
<title>Alpakas vom Lindenbruch – Wickelfalz-Flyer</title>
<link href="https://fonts.googleapis.com/css2?family=Lilita+One&family=Kalam:wght@400&family=Lato:wght@400;700&display=swap" rel="stylesheet">
<style>
  :root{
    --green-light:#5f7545;
    --green-dark:#46591f;
    --sand-dark:#e2ae66;
    --sand-light:#f2cf9c;
    --maroon:#6e1a1c;
    --cream:#f6e8cc;
    --white:#ffffff;
    --photo-meadow:#8d9a63;
    --photo-fur:#a27a52;
    --photo-dark:#5a3528;
    --photo-pale:#c9b08c;
  }
  *{margin:0;padding:0;box-sizing:border-box}
  html,body{width:857px;height:1200px;overflow:hidden;background:var(--white)}
  .sheet{position:relative;width:857px;height:1200px}
  .panel{position:absolute;width:242px;height:484px;overflow:hidden}
  .panel > svg{position:absolute;inset:0;width:242px;height:484px}
  .row-top{top:94px}.row-bottom{top:592px}
  .col-1{left:46px}.col-2{left:297px}.col-3{left:548px}
  .abs{position:absolute}
  .headline{
    font-family:"Lilita One",sans-serif;font-weight:400;color:var(--maroon);letter-spacing:.6px;line-height:1.15;white-space:nowrap;
    text-shadow:1px 0 var(--cream),-1px 0 var(--cream),0 1px var(--cream),0 -1px var(--cream),
      1px 1px var(--cream),-1px -1px var(--cream),1px -1px var(--cream),-1px 1px var(--cream);
  }
  .centered{left:0;width:242px;text-align:center}
  .body-copy{font-family:"Lato",sans-serif;font-size:8.4px;line-height:10.8px}
  .on-green{color:var(--cream)}
  .on-sand{color:var(--maroon)}
  .contact-line{display:flex;align-items:center;gap:8px;font-family:"Lato",sans-serif;font-size:8.2px;color:var(--maroon)}
  .leaf{width:9px;height:10px;flex:none}
  .offer-title{font-family:"Lato",sans-serif;font-weight:700;font-size:10px;color:var(--cream);margin-bottom:1px}
  .offer{position:absolute;left:12px;width:226px;display:flex;align-items:center;gap:6px}
  .offer p{font-family:"Lato",sans-serif;font-size:8.2px;line-height:10.8px;color:var(--maroon);white-space:nowrap}
  .list{position:absolute;left:11px;top:341px;width:220px;list-style:none}
  .list li{display:flex;align-items:center;gap:5px;font-family:"Lato",sans-serif;font-size:8.2px;line-height:9.4px;color:var(--maroon);margin-bottom:9.4px}
  .welcome-script{font-family:"Kalam",cursive;color:var(--cream)}
  .welcome-name{font-family:"Lilita One",sans-serif;color:var(--cream);text-align:center;letter-spacing:.4px}
</style>
</head>
<body>
<svg width="0" height="0" style="position:absolute">
  <defs>
    <linearGradient id="greenFade" x1="0" y1="0" x2="0" y2="1"><stop offset="0" stop-color="#5f7545"/><stop offset="1" stop-color="#46591f"/></linearGradient>
    <linearGradient id="sandFade" x1="0" y1="0" x2="0" y2="1"><stop offset="0" stop-color="#e2ae66"/><stop offset="1" stop-color="#f2cf9c"/></linearGradient>
    <linearGradient id="sandFadeUp" x1="0" y1="1" x2="1" y2="0"><stop offset="0" stop-color="#e2ae66"/><stop offset="1" stop-color="#f2cf9c"/></linearGradient>
    <radialGradient id="softGlowLight"><stop offset="0" stop-color="#f6e8cc" stop-opacity=".16"/><stop offset="1" stop-color="#f6e8cc" stop-opacity="0"/></radialGradient>
    <radialGradient id="softGlowGreen"><stop offset="0" stop-color="#8d9a63" stop-opacity=".28"/><stop offset="1" stop-color="#8d9a63" stop-opacity="0"/></radialGradient>
    <symbol id="leafIcon" viewBox="0 0 10 11"><path d="M9 0C4 1 0 4 1 9c.3 1 1 1.5 2 1.5C3 7 5 4 8 2 6 5 4 8 4 10.5 8 10 10 5 9 0Z" fill="#5f7545"/></symbol>
    <clipPath id="aboutClip"><rect x="0" y="27" width="224" height="300"/></clipPath>
  </defs>
</svg>

<main class="sheet">

  <!-- Wer sind wir -->
  <section class="panel row-top col-1">
    <svg viewBox="0 0 242 484">
      <rect width="242" height="484" fill="url(#greenFade)"/>
      <path d="M18 19H205Q224 19 224 38V283Q160 290 100 288Q30 280 18 200Z" fill="url(#sandFadeUp)"/>
      <g clip-path="url(#aboutClip)">
        <circle cx="168" cy="138" r="125" fill="none" stroke="#f6e8cc" stroke-width="1"/>
        <circle cx="172" cy="138" r="116" fill="var(--photo-meadow)" role="img" aria-label="Foto: Lama auf einer Wiese vor Waldrand"/>
      </g>
      <ellipse cx="205" cy="420" rx="40" ry="60" fill="url(#softGlowGreen)" role="img" aria-label="Linienzeichnung eines Alpakas"/>
    </svg>
    <h2 class="headline abs" style="left:20px;top:265px;font-size:19px">WER SIND WIR?</h2>
    <p class="body-copy on-green abs" style="left:21px;top:302px;width:215px">
      Wir – Lena und Jonas Wiegand –<br>leben gemeinsam mit unseren drei Töchtern,<br>unseren Alpakas, Hunden und Pferden<br>auf einem idyllischen Bauernhof in Rethfeld,<br>nahe der niederländischen Grenze.<br><br>
      Seit 2021 sind Alpakas ein fester Bestandteil<br>unseres Lebens. Mit viel Sorgfalt, Respekt<br>und Begeisterung widmen wir uns ihrer<br>Haltung und Pflege.<br>Für uns sind sie nicht nur Tiere,<br>sondern ruhige Begleiter, die den besonderen<br>Charakter unseres Hofes prägen.
    </p>
  </section>

  <!-- Kontakt -->
  <section class="panel row-top col-2">
    <svg viewBox="0 0 242 484">
      <rect width="242" height="484" fill="url(#sandFade)"/>
      <path d="M0 385Q20 395 50 395Q90 390 120 340Q160 280 200 275Q225 272 242 278V484H0Z" fill="url(#greenFade)"/>
      <ellipse cx="55" cy="300" rx="45" ry="62" fill="url(#softGlowLight)" role="img" aria-label="Linienzeichnung eines Alpakas"/>
      <ellipse cx="172" cy="410" rx="58" ry="70" fill="url(#softGlowGreen)" role="img" aria-label="Linienzeichnung eines Alpakas"/>
    </svg>
    <h2 class="headline abs centered" style="top:40px;font-size:23px;letter-spacing:1px">UNSER&nbsp; KONTAKT</h2>
    <p class="body-copy on-sand abs" style="left:70px;top:94px">Alpakas vom Lindenbruch<br>Lindenbrucher Hof<br>41899 Wiesenkamp</p>
    <div class="contact-line abs" style="left:54px;top:137px"><svg class="leaf"><use href="#leafIcon"/></svg>+49 (0)160 000 123 4</div>
    <div class="contact-line abs" style="left:54px;top:159px"><svg class="leaf"><use href="#leafIcon"/></svg>info@alpakas-vom-lindenbruch.de</div>
    <div class="contact-line abs" style="left:54px;top:180px"><svg class="leaf"><use href="#leafIcon"/></svg>www.alpakas-vom-lindenbruch.de</div>
  </section>

  <!-- Titel -->
  <section class="panel row-top col-3">
    <svg viewBox="0 0 242 484">
      <rect width="242" height="484" fill="url(#greenFade)"/>
      <path d="M19 17H225V210Q210 300 125 305Q40 300 19 240Z" fill="var(--photo-fur)" role="img" aria-label="Foto: Alpaka mit braunem Vlies auf einer Weide"/>
      <path d="M218 236Q195 305 120 300" fill="none" stroke="#e2ae66" stroke-width="1"/>
      <ellipse cx="42" cy="370" rx="30" ry="50" fill="url(#softGlowGreen)" role="img" aria-label="Linienzeichnung eines Alpakas"/>
      <ellipse cx="195" cy="420" rx="45" ry="60" fill="url(#softGlowGreen)" role="img" aria-label="Linienzeichnung eines Alpakas"/>
    </svg>
    <h1 class="headline abs centered" style="top:323px;font-size:24px">WILLKOMMEN</h1>
    <p class="welcome-script abs centered" style="top:368px;font-size:16px">bei den</p>
    <p class="welcome-name abs" style="left:0;width:242px;top:392px;font-size:21px">Alpakas</p>
    <p class="welcome-name abs" style="left:0;width:242px;top:419px;font-size:19px">vom Lindenbruch</p>
  </section>

  <!-- Warum Alpakas -->
  <section class="panel row-bottom col-1">
    <svg viewBox="0 0 242 484">
      <rect width="242" height="484" fill="url(#greenFade)"/>
      <path d="M242 205Q215 290 150 325Q90 350 20 345Q5 345 0 350V484H242Z" fill="url(#sandFadeUp)"/>
      <circle cx="190" cy="78" r="73" fill="none" stroke="#f2cf9c" stroke-width="1"/>
      <circle cx="190" cy="78" r="68" fill="var(--photo-dark)" role="img" aria-label="Foto: Kopf eines braun-weißen Alpakas"/>
      <circle cx="64" cy="419" r="76" fill="none" stroke="#f6e8cc" stroke-width="1"/>
      <circle cx="60" cy="419" r="71" fill="var(--photo-pale)" role="img" aria-label="Foto: zwei helle Alpakas nebeneinander"/>
    </svg>
    <h2 class="headline abs" style="left:25px;top:108px;font-size:23px;line-height:30px">WARUM<br>ALPAKAS?</h2>
    <p class="body-copy on-green abs" style="left:24px;top:185px;width:210px">
      Alpakas begegnen<br>Menschen mit einer sanften,<br>aufmerksamen Art. Zeit mit<br>ihnen zu verbringen bedeutet,<br>langsamer zu werden,<br>die Natur bewusster wahrzunehmen<br>und den Moment zu genießen.<br>Unsere Angebote richten sich an alle,<br>die Entspannung suchen und dem Alltag<br>für eine Weile entfliehen möchten.
    </p>
  </section>

  <!-- Angebote -->
  <section class="panel row-bottom col-2">
    <svg viewBox="0 0 242 484">
      <rect width="242" height="484" fill="url(#sandFade)"/>
      <path d="M0 325Q30 350 70 350Q110 348 140 330Q200 295 242 310V484H0Z" fill="url(#greenFade)"/>
      <ellipse cx="165" cy="410" rx="70" ry="62" fill="url(#softGlowGreen)" role="img" aria-label="Linienzeichnung zweier Alpakas"/>
    </svg>
    <h2 class="headline abs centered" style="top:26px;font-size:23px;letter-spacing:1px">UNSERE&nbsp; ANGEBOTE</h2>
    <div class="offer" style="top:73px"><svg class="leaf" style="width:12px;height:14px"><use href="#leafIcon"/></svg>
      <div><div class="offer-title">Alpaka &amp; Lama-Wanderungen</div><p>In ruhigem Tempo spazieren Sie Seite an Seite<br>mit unseren Tieren durch die Natur.<br>Die Wanderungen bieten Raum für Entschleunigung,<br>Beobachtung und kleine Gespräche – ein Erlebnis für<br>Einzelpersonen, Paare und Familien.</p></div></div>
    <div class="offer" style="top:151px"><svg class="leaf" style="width:12px;height:14px"><use href="#leafIcon"/></svg>
      <div><div class="offer-title">Alpaka-Begegnungen</div><p>Bei einer persönlichen Begegnung lernen Sie unsere<br>Alpakas in entspannter Atmosphäre kennen.<br>Ob ruhiges Zusammensein, eine Schnupperstunde oder<br>ein Picknick – der Fokus liegt auf Nähe, Achtsamkeit<br>und Zeit ohne Eile.</p></div></div>
    <div class="offer" style="top:229px"><svg class="leaf" style="width:12px;height:14px"><use href="#leafIcon"/></svg>
      <div><div class="offer-title">Hofladen</div><p>In unserem Hofladen finden Sie ausgewählte<br>Produkte rund um das Alpaka:<br>hochwertige Alpakawolle, handgefertigte Mode sowie<br>besondere Geschenkideen – nachhaltig hergestellt und<br>mit Liebe ausgewählt.</p></div></div>
  </section>

  <!-- Gutscheine -->
  <section class="panel row-bottom col-3">
    <svg viewBox="0 0 242 484">
      <rect width="242" height="484" fill="url(#greenFade)"/>
      <path d="M0 245Q60 250 110 248Q170 250 200 330Q225 380 242 415V484H0Z" fill="url(#sandFadeUp)"/>
      <circle cx="163" cy="253" r="77" fill="none" stroke="#f2cf9c" stroke-width="1"/>
      <circle cx="166" cy="251" r="72" fill="var(--photo-dark)" role="img" aria-label="Foto: Kopf eines dunkelbraunen Alpakas"/>
    </svg>
    <h2 class="headline abs centered" style="top:56px;font-size:24px;letter-spacing:.6px">GUTSCHEINE</h2>
    <p class="body-copy on-green abs" style="left:59px;top:101px;width:170px;line-height:11.6px">Alle Alpaka- und Lama-Erlebnisse<br>sind auch als Gutschein erhältlich<br>und eignen sich als persönliche<br>Aufmerksamkeit für besondere<br>Momente.</p>
    <div class="offer-title abs" style="left:24px;top:314px">Wir bieten an:</div>
    <ul class="list">
      <li><svg class="leaf"><use href="#leafIcon"/></svg>Alpaka- und Lamawanderungen</li>
      <li><svg class="leaf"><use href="#leafIcon"/></svg>Picknick mit Alpakas und Lamas</li>
      <li><svg class="leaf"><use href="#leafIcon"/></svg>Schnupperstunden / Kennenlernen</li>
      <li><svg class="leaf"><use href="#leafIcon"/></svg>Betriebsausflüge &amp; Gruppenangebote</li>
      <li><svg class="leaf"><use href="#leafIcon"/></svg>Junggesellenabschiede</li>
      <li><svg class="leaf"><use href="#leafIcon"/></svg><span>Persönlich geführt, familiär,<br>mit viel Herzblut und echter<br>Begeisterung für Alpakas und Lamas</span></li>
    </ul>
  </section>

</main>
</body>
</html>
```